Dental Plan for Dogs

We are a vet clinic and I am wanting a poster designed that can then ultimately be changed/rejigged to be use on a website/facebook as a banner ad that promotes dental health in dogs. Therefore I will need the photoshop files as well as pngs/pdfs.
I want a dog and a cat in the image used for the poster with them showing healthy teeth and looking happy!
The feels is to be professional but also cute/funny. Using the orange coming through from the logo and the logo somewhere on the poster.
The text as below
Heading: Join our Dental Bluebell Plan!
Text: Keep your fur child smiling all year round while we cap their dental work at $365 if they return for a dental clean within 365 days! The plan includes full mouth dental x-rays and scale and polish of all teeth under a carefully monitored general anaesthetic! That'll give you both a reason to smile and save you over $180 per dental! *
Conditions (in smaller writing): *Any extractions and more advanced dental procedures if required will incur an additional cost that will be discussed with your prior to the procedure.
Thanks

```html
<!DOCTYPE html>
<html lang="en">
<head>
<meta charset="utf-8">
<title>Dental Bluebell Plan Poster</title>
<link rel="stylesheet" href="https://fonts.googleapis.com/css2?family=Anton&family=Delius&family=Dancing+Script:wght@600&family=Arimo:wght@400;700&display=swap">
<style>
  :root {
    --bg: #f1f0ec;
    --paper: #ffffff;
    --grey-light: #e4e4e4;
    --grey-mid: #cfcfcf;
    --orange: #f39c22;
    --orange-deep: #ee8f16;
    --ink: #2b2b2b;
    --white: #ffffff;
  }
  * { margin: 0; padding: 0; box-sizing: border-box; }
  html, body { width: 1200px; height: 1200px; overflow: hidden; background: var(--bg); }
  .canvas { position: relative; width: 1200px; height: 1200px; }
  .poster {
    position: absolute; left: 155px; top: 9px;
    width: 848px; height: 1125px;
    background: var(--paper);
    transform: scale(1.05); transform-origin: top left;
  }
  .poster-field {
    position: absolute; left: 20px; top: 22px; width: 808px; height: 1081px;
    background: linear-gradient(160deg, var(--grey-light) 0%, #d9d9d9 55%, var(--grey-mid) 100%);
    overflow: hidden;
  }
  .logo-cloud {
    position: absolute; left: 470px; top: -40px; width: 380px; height: 190px;
    background: var(--white); border-radius: 50%;
  }
  .headline-join {
    position: absolute; left: 55px; top: 40px;
    font-family: "Anton", sans-serif; font-size: 128px; line-height: 1;
    color: var(--orange); letter-spacing: -3px;
    text-shadow: 4px 4px 0 #5b5b5b;
  }
  .headline-plan {
    position: absolute; left: 140px; top: 175px;
    font-family: "Delius", sans-serif; font-size: 62px; line-height: 1;
    color: var(--ink); white-space: nowrap;
  }
  .clinic-mark {
    position: absolute; left: 520px; top: 32px; width: 200px; text-align: center;
    font-family: "Delius", sans-serif; color: var(--orange);
  }
  .clinic-name { display: flex; align-items: center; justify-content: center; gap: 8px; font-size: 30px; line-height: 1; }
  .clinic-dot { width: 18px; height: 18px; border-radius: 50%; background: var(--orange); flex: none; }
  .clinic-type { font-size: 10px; letter-spacing: 2px; color: var(--ink); margin-top: 6px; }
  .clinic-location { font-family: "Arimo", sans-serif; font-size: 15px; margin-top: 6px; border-top: 1px solid var(--orange); padding-top: 4px; display: inline-block; }
  .art-dog {
    position: absolute; left: 40px; top: 280px; width: 385px; height: 253px;
    background: linear-gradient(180deg, #e9e9e9, #dcdcdc); border-radius: 40px 40px 0 0;
  }
  .art-cat {
    position: absolute; left: 465px; top: 750px; width: 305px; height: 325px;
    background: linear-gradient(180deg, #dedede, #d2d2d2); border-radius: 50% 50% 20px 20px;
  }
  .smile-note {
    position: absolute; left: 450px; top: 370px; width: 320px;
    font-family: "Dancing Script", cursive; font-size: 47px; line-height: 61px;
    color: var(--ink); transform: rotate(-8deg); transform-origin: left top;
  }
  .smile-note .saving { color: var(--orange); }
  .offer-box {
    position: absolute; left: 0; top: 533px; width: 443px; height: 395px;
    background: linear-gradient(135deg, var(--orange) 0%, var(--orange-deep) 100%);
    padding: 14px 22px 0 26px; color: var(--ink);
  }
  .offer-lead {
    font-family: "Anton", sans-serif; font-size: 37px; line-height: 47px;
    color: var(--white); letter-spacing: -0.5px; text-shadow: 1px 1px 0 rgba(0,0,0,.25);
  }
  .offer-lead strong { color: var(--ink); font-weight: 400; text-shadow: none; }
  .offer-detail { font-family: "Arimo", sans-serif; font-size: 17.5px; line-height: 23px; margin-top: 18px; }
  .offer-conditions { font-family: "Arimo", sans-serif; font-size: 10.5px; line-height: 14px; margin-top: 18px; color: var(--white); }
  .pointer-arrow { position: absolute; left: 380px; top: 740px; }
  .contact { position: absolute; left: 26px; top: 985px; font-family: "Anton", sans-serif; font-size: 29px; line-height: 40px; letter-spacing: -0.5px; }
  .contact-email { color: var(--orange); }
  .contact-web { color: var(--ink); }
</style>
</head>
<body>
<div class="canvas">
  <div class="poster">
    <div class="poster-field">
      <div class="logo-cloud"></div>
      <div class="clinic-mark">
        <div class="clinic-name"><span class="clinic-dot"></span>Dr Whiskers</div>
        <div class="clinic-type">VETERINARY CLINIC</div>
        <div class="clinic-location">MAPLE HILL</div>
      </div>

      <h1 class="headline-join">Join our</h1>
      <h2 class="headline-plan">Dental Bluebell Plan!</h2>

      <div class="art-dog" role="img" aria-label="Line drawing of a happy dog grinning to show healthy teeth"></div>

      <p class="smile-note">That'll give you both a reason to smile and save you over <span class="saving">$180</span> per dental! *</p>

      <div class="offer-box">
        <p class="offer-lead">Keep your fur child smiling all year round while we cap their <strong>dental work at 365</strong> if they return for a dental clean within 365 days!</p>
        <p class="offer-detail">The plan includes <b>full mouth</b> dental x-rays and scale and polish of all teeth under a carefully monitored general anaesthetic!</p>
        <p class="offer-conditions">*Any extractions and more advanced dental procedures if required will incur an additional cost that will be discussed with your prior to the procedure.</p>
      </div>

      <svg class="pointer-arrow" width="180" height="80" viewBox="0 0 180 80" aria-hidden="true">
        <path d="M8 16 C 40 70, 110 70, 160 28" fill="none" stroke="#ffffff" stroke-width="3" stroke-linecap="round"/>
        <path d="M146 22 L166 12 L160 34 Z" fill="#ffffff"/>
      </svg>

      <div class="art-cat" role="img" aria-label="Line drawing of a cheerful cat smiling with its teeth showing"></div>

      <div class="contact">
        <div class="contact-email">info@harbourvetgroup.com.au</div>
        <div class="contact-web">www.drwhiskersvet.com.au</div>
      </div>
    </div>
  </div>
</div>
</body>
</html>
```